Website Design for Gold Buying Company in Australia

We are looking for a Website layout for a company who buy gold pieces from trade and the public.

They would like to communicate that its easy, safe, a great way to make more money, and they pay the best prices in australia for Gold jewelery

Target Market(s)

Adults based in Australia aged 25-60 who are looking to make some extra money

Industry/Entity Type

It Company

Number of Pages Required

2 pages

Requirements
Must have
• Must have a homepage and a page to use for content.

• Will have a feed for the latest Gold, silver and platinum prices they are buying and selling at.

• Needs to have a from on the homepage where people can submit their details to be sent a ''Treasure Pouch'' which allows them to send gold pieces to eb valued and bought by the company.

Nice to have
• Would be nice to have a steped out graphic of how the ''Treasure Pouch by mail'' process works [Request a Kit, Send in your Gold, We Value and grade it, We pay you cash, cheque of Direct Deposit]

• Imagery will be gold related

• Colour schemes are not a major Issue-but using some gold or silver would be a good idea
Should not have
• No cheesy gold graphics please :)

```html
<!DOCTYPE html>
<html lang="en">
<head>
<meta charset="utf-8">
<title>Aurum Exchange – Website Pages</title>
<link href="https://fonts.googleapis.com/css2?family=Raleway:wght@200;300;400&family=Arimo:wght@400;700&display=swap" rel="stylesheet">
<style>
:root{
  --stage:#0b0b0b;
  --paper:#ffffff;
  --gold-dark:#6e5512;
  --gold-mid:#a8871f;
  --gold-light:#d9c35a;
  --gold-text:#9c7d1c;
  --gold-head:#8a6d16;
  --grey-bar:#8d8d8d;
  --grey-dark:#3a3a3a;
  --body-text:#8a8a8a;
  --table-text:#444;
  --white:#ffffff;
  --yellow:#f3dc57;
}
*{box-sizing:border-box;margin:0;padding:0}
html,body{width:1200px;height:3020px;overflow:hidden;background:var(--stage)}
body{font-family:"Arimo",Arial,sans-serif;position:relative}
.page{position:absolute;left:40px;width:1120px;height:900px;background:var(--paper);overflow:hidden}
.page--home{top:80px}
.page--how{top:1060px}
.page--form{top:2040px}

/* header */
.site-header{position:absolute;left:0;top:0;width:100%;height:160px;
  background:linear-gradient(100deg,var(--gold-dark) 0%,var(--gold-mid) 35%,var(--gold-light) 65%,var(--gold-mid) 85%,var(--gold-dark) 100%);
  border-top:5px solid var(--gold-light)}
.site-header::after{content:"";position:absolute;left:0;right:0;bottom:0;height:30px;background:linear-gradient(to bottom,rgba(80,60,10,0),rgba(80,60,10,.5))}
.brand{position:absolute;left:110px;top:38px;font-family:"Raleway",sans-serif;font-weight:300;font-size:68px;letter-spacing:2px;color:var(--white);line-height:1}
.tagline{position:absolute;left:256px;top:113px;font-family:"Arimo",sans-serif;font-size:19px;color:var(--yellow);letter-spacing:.5px}
.account-links{position:absolute;right:55px;top:20px;font-size:13px;color:var(--white)}
.account-links span{margin:0 6px;opacity:.6}

.main-nav{position:absolute;left:0;top:160px;width:100%;height:32px;background:linear-gradient(to bottom,#a9a9a9,#6f6f6f);display:flex;justify-content:flex-end;align-items:center;padding-right:42px;gap:0}
.main-nav a{font-size:11px;color:var(--white);text-decoration:none;padding:7px 13px;letter-spacing:-.2px}
.main-nav a.is-active{background:#2a2a2a;color:var(--white)}

/* sidebar */
.sidebar{position:absolute;left:45px;top:212px;width:165px}
.kit-image{width:140px;height:150px;margin-left:18px;background:linear-gradient(135deg,#c7a634,#6b4f0e);}
.kit-cta{margin-top:-6px;height:86px;border:5px solid var(--gold-mid);border-top:none;background:linear-gradient(to bottom,#b89524,#7c5f12);color:var(--white);text-align:center;padding-top:6px}
.kit-cta b{display:block;font-size:22px;letter-spacing:.3px}
.kit-cta span{display:block;font-size:14px;line-height:18px}
.values-head{margin-top:36px;height:50px;background:linear-gradient(to bottom,#c4a32f,#7a5e12);border:3px solid #d8c26a;color:var(--white);font-size:13px;line-height:14px;padding:10px 12px}
.price-block{margin-top:12px;padding-left:5px}
.price-block h3{font-size:11px;color:var(--gold-text);font-weight:700;margin-bottom:2px}
.price-block table{width:158px;border-collapse:collapse;font-size:8px;color:var(--table-text)}
.price-block td{padding:1px 0;line-height:12px}
.price-block tr:first-child td{font-weight:700}
.price-block td:nth-child(2){width:70px}
.price-block td:nth-child(3){text-align:right}

/* footer */
.site-footer{position:absolute;left:0;bottom:0;width:100%;height:42px;background:linear-gradient(90deg,#555,#8a8a8a 50%,#555);color:#eee;font-size:13px;text-align:right;padding:13px 55px 0 0}

/* home */
.hero-photo{position:absolute;left:256px;top:212px;width:270px;height:392px;background:linear-gradient(160deg,#e9e1d6,#6e86b0 45%,#c9473a 80%,#f1ece4)}
.hero-copy{position:absolute;left:548px;top:258px;font-family:"Raleway",sans-serif;color:var(--gold-head);font-weight:300;line-height:1}
.hero-copy .sm{display:block;font-size:31px;letter-spacing:1px;margin:10px 0 8px}
.hero-copy .lg{display:block;font-size:72px;letter-spacing:1px}
.hero-rule{position:absolute;left:256px;top:604px;width:810px;height:2px;background:linear-gradient(90deg,#e5d9b2,#c3a54a,#e5d9b2)}
.feature{position:absolute;top:620px;width:388px}
.feature--guide{left:256px}
.feature--tell{left:668px}
.feature h2{font-family:"Raleway",sans-serif;font-weight:300;font-size:20px;color:var(--gold-text);margin-bottom:10px}
.feature p{font-size:12px;color:var(--body-text);line-height:16px;text-align:justify}
.btn{display:inline-block;background:linear-gradient(to bottom,#b0902a,#6c520f);color:var(--white);font-size:13px;padding:8px 10px;box-shadow:0 3px 3px rgba(0,0,0,.3);text-decoration:none}
.feature .btn{margin-top:14px}

/* how it works */
.page-title{position:absolute;left:255px;top:228px;font-family:"Raleway",sans-serif;font-weight:300;font-size:37px;color:var(--gold-head);letter-spacing:2px}
.steps{position:absolute;left:256px;top:292px;width:600px;list-style:none}
.step{display:flex;height:121px}
.step-image{width:264px;height:98px;border:4px solid #8e6f1a;flex:none}
.step-image--kit{background:linear-gradient(90deg,#6b4f0e,#c9a93a,#5c430b)}
.step-image--gold{background:linear-gradient(135deg,#f3e6df,#c9894a,#f0d9cf)}
.step-image--value{background:linear-gradient(135deg,#6b5a10,#d9c34a,#8a7a20)}
.step-image--paid{background:linear-gradient(135deg,#3f8a6a,#b7cfb2,#e8ddd2)}
.step-body{margin-left:28px;width:290px}
.step h2{display:flex;align-items:center;font-family:"Raleway",sans-serif;font-weight:300;font-size:20px;color:var(--gold-text);margin-bottom:8px}
.step-num{display:inline-flex;align-items:center;justify-content:center;width:28px;height:28px;background:#8a6a14;color:var(--white);font-family:"Arimo",sans-serif;font-weight:700;font-size:20px;margin-right:8px}
.step p{font-size:12px;line-height:15px;color:var(--body-text)}

/* form */
.item-form{position:absolute;left:256px;top:335px;width:300px}
.item-form h2{font-family:"Raleway",sans-serif;font-weight:300;font-size:20px;color:var(--gold-text);margin-bottom:12px}
.field-row{display:flex;gap:10px;margin-bottom:10px}
.field label{display:block;font-size:9px;color:var(--body-text);text-align:center;margin-top:3px}
.field input,.field textarea{border:1px solid #c9c9c9;height:20px;display:block;background:var(--white)}
.field textarea{height:106px;width:288px;resize:none}
.field .desc{text-align:left}
.item-form .btn{margin-top:14px;padding:5px 9px;font-size:13px}
</style>
</head>
<body>

<!-- HOME -->
<section class="page page--home">
  <header class="site-header">
    <div class="brand">AURUM EXCHANGE</div>
    <div class="tagline">BEST PRICES IN AUSTRALIA</div>
    <div class="account-links">Sign in<span>|</span>Account Settings</div>
  </header>
  <nav class="main-nav">
    <a>HOME</a><a>ABOUT US</a><a>WHAT WE BUY &amp; SELL</a><a>HOW IT WORKS</a><a>COMMEN QUESTIONS</a><a>BULLION</a><a>CONTACT US</a><a class="is-active">TRADE ENQUIRIES</a>
  </nav>
  <aside class="sidebar">
    <div class="kit-image" role="img" aria-label="Gold pouch packaging"></div>
    <div class="kit-cta"><b>CLICK HERE</b><span>TO PURCHASE YOUR</span><span>TREASURE POUCH</span></div>
    <div class="values-head">CURRENT<br>COMMODITY VALUES</div>
    <div class="price-block"><h3>Gold Price Performance</h3><table><tr><td>Change</td><td>Amount</td><td>%</td></tr><tr><td>Today</td><td>11.17</td><td>1.11%</td></tr><tr><td>30 Days</td><td>84.60</td><td>9.05%</td></tr><tr><td>6 Months</td><td>94.83</td><td>10.26%</td></tr></table></div>
    <div class="price-block"><h3>Silver Price Performance</h3><table><tr><td>Change</td><td>Amount</td><td>%</td></tr><tr><td>Today</td><td>11.17</td><td>1.11%</td></tr><tr><td>30 Days</td><td>84.60</td><td>9.05%</td></tr><tr><td>6 Months</td><td>94.83</td><td>10.26%</td></tr></table></div>
    <div class="price-block"><h3>Platinum Price Performance</h3><table><tr><td>Change</td><td>Amount</td><td>%</td></tr><tr><td>Today</td><td>11.17</td><td>1.11%</td></tr><tr><td>30 Days</td><td>84.60</td><td>9.05%</td></tr><tr><td>6 Months</td><td>94.83</td><td>10.26%</td></tr></table></div>
  </aside>
  <div class="hero-photo" role="img" aria-label="Happy couple holding a fan of cash"></div>
  <h1 class="hero-copy">
    <span class="sm" style="margin-top:0">THE SAFEST WAY FOR</span>
    <span class="lg">AUSTRALIANS</span>
    <span class="sm">TO TURN</span>
    <span class="lg">GOLD</span>
    <span class="sm">INTO</span>
    <span class="lg">CASH</span>
  </h1>
  <div class="hero-rule"></div>
  <div class="feature feature--guide">
    <h2>WE GUIDE YOU THROUGH THE HASSLE</h2>
    <p>In at est mauris. Sed placerat feugiat libero a auctor. Sed aliquet varius neque, in pulvinar sem iaculis nec. Aenean ut orci libero. Nullam a est dolor. Mauris orci nisi, aliquam ac suscipit ut, lacinia.</p>
    <a class="btn">HOW IT WORKS</a>
  </div>
  <div class="feature feature--tell">
    <h2>LET US KNOW ABOUT YOUR GOLD</h2>
    <p>In at est mauris. Sed placerat feugiat libero a auctor. Sed aliquet varius neque, in pulvinar sem iaculis nec. Aenean ut orci libero. Nullam a est dolor. Mauris orci nisi, aliquam ac suscipit ut, lacinia nec</p>
    <a class="btn">CHECK IT OUT</a>
  </div>
  <footer class="site-footer">©2009 Aurum Exchange Australia Pty LTD</footer>
</section>

<!-- HOW IT WORKS -->
<section class="page page--how">
  <header class="site-header">
    <div class="brand">AURUM EXCHANGE</div>
    <div class="tagline">BEST PRICES IN AUSTRALIA</div>
    <div class="account-links">Sign in<span>|</span>Account Settings</div>
  </header>
  <nav class="main-nav">
    <a>HOME</a><a>ABOUT US</a><a>WHAT WE BUY &amp; SELL</a><a>HOW IT WORKS</a><a>COMMEN QUESTIONS</a><a>BULLION</a><a>CONTACT US</a><a class="is-active">TRADE ENQUIRIES</a>
  </nav>
  <aside class="sidebar">
    <div class="kit-image" role="img" aria-label="Gold pouch packaging"></div>
    <div class="kit-cta"><b>CLICK HERE</b><span>TO PURCHASE YOUR</span><span>TREASURE POUCH</span></div>
    <div class="values-head">CURRENT<br>COMMODITY VALUES</div>
    <div class="price-block"><h3>Gold Price Performance</h3><table><tr><td>Change</td><td>Amount</td><td>%</td></tr><tr><td>Today</td><td>11.17</td><td>1.11%</td></tr><tr><td>30 Days</td><td>84.60</td><td>9.05%</td></tr><tr><td>6 Months</td><td>94.83</td><td>10.26%</td></tr></table></div>
    <div class="price-block"><h3>Silver Price Performance</h3><table><tr><td>Change</td><td>Amount</td><td>%</td></tr><tr><td>Today</td><td>11.17</td><td>1.11%</td></tr><tr><td>30 Days</td><td>84.60</td><td>9.05%</td></tr><tr><td>6 Months</td><td>94.83</td><td>10.26%</td></tr></table></div>
    <div class="price-block"><h3>Platinum Price Performance</h3><table><tr><td>Change</td><td>Amount</td><td>%</td></tr><tr><td>Today</td><td>11.17</td><td>1.11%</td></tr><tr><td>30 Days</td><td>84.60</td><td>9.05%</td></tr><tr><td>6 Months</td><td>94.83</td><td>10.26%</td></tr></table></div>
  </aside>
  <h1 class="page-title">HOW IT WORKS</h1>
  <ol class="steps">
    <li class="step"><div class="step-image step-image--kit" role="img" aria-label="Close-up of the gold pouch packaging"></div><div class="step-body"><h2><span class="step-num">1</span>PURCHASE OUR KIT</h2><p>Lorem ipsum dolor sit amet, consectetur adipisc elit. Nullam malesuada dapibus convallis. Sed a lacus et diam cursus. Lorem ipsum dolor sit amet, consectetur</p></div></li>
    <li class="step"><div class="step-image step-image--gold" role="img" aria-label="Hand holding gold jewellery"></div><div class="step-body"><h2><span class="step-num">2</span>SEND IN YOUR GOLD</h2><p>Lorem ipsum dolor sit amet, consectetur adipisc elit. Nullam malesuada dapibus convallis. Sed a lacus et diam cursus. Lorem ipsum dolor sit amet, consectetur</p></div></li>
    <li class="step"><div class="step-image step-image--value" role="img" aria-label="Gold bar with glowing light"></div><div class="step-body"><h2><span class="step-num">3</span>WE VALUE YOUR GOLD</h2><p>Lorem ipsum dolor sit amet, consectetur adipisc elit. Nullam malesuada dapibus convallis. Sed a lacus et diam cursus. Lorem ipsum dolor sit amet, consectetur</p></div></li>
    <li class="step"><div class="step-image step-image--paid" role="img" aria-label="Hand holding Australian banknotes"></div><div class="step-body"><h2><span class="step-num">4</span>YOU GET PAID</h2><p>Lorem ipsum dolor sit amet, consectetur adipisc elit. Nullam malesuada dapibus convallis. Sed a lacus et diam cursus. Lorem ipsum dolor sit amet, consectetur</p></div></li>
  </ol>
  <footer class="site-footer">©2009 Aurum Exchange Australia Pty LTD</footer>
</section>

<!-- FORM -->
<section class="page page--form">
  <header class="site-header">
    <div class="brand">AURUM EXCHANGE</div>
    <div class="tagline">BEST PRICES IN AUSTRALIA</div>
    <div class="account-links">Sign in<span>|</span>Account Settings</div>
  </header>
  <nav class="main-nav">
    <a>HOME</a><a>ABOUT US</a><a>WHAT WE BUY &amp; SELL</a><a>HOW IT WORKS</a><a>COMMEN QUESTIONS</a><a>BULLION</a><a>CONTACT US</a><a class="is-active">TRADE ENQUIRIES</a>
  </nav>
  <aside class="sidebar">
    <div class="kit-image" role="img" aria-label="Gold pouch packaging"></div>
    <div class="kit-cta"><b>CLICK HERE</b><span>TO PURCHASE YOUR</span><span>TREASURE POUCH</span></div>
    <div class="values-head">CURRENT<br>COMMODITY VALUES</div>
    <div class="price-block"><h3>Gold Price Performance</h3><table><tr><td>Change</td><td>Amount</td><td>%</td></tr><tr><td>Today</td><td>11.17</td><td>1.11%</td></tr><tr><td>30 Days</td><td>84.60</td><td>9.05%</td></tr><tr><td>6 Months</td><td>94.83</td><td>10.26%</td></tr></table></div>
    <div class="price-block"><h3>Silver Price Performance</h3><table><tr><td>Change</td><td>Amount</td><td>%</td></tr><tr><td>Today</td><td>11.17</td><td>1.11%</td></tr><tr><td>30 Days</td><td>84.60</td><td>9.05%</td></tr><tr><td>6 Months</td><td>94.83</td><td>10.26%</td></tr></table></div>
    <div class="price-block"><h3>Platinum Price Performance</h3><table><tr><td>Change</td><td>Amount</td><td>%</td></tr><tr><td>Today</td><td>11.17</td><td>1.11%</td></tr><tr><td>30 Days</td><td>84.60</td><td>9.05%</td></tr><tr><td>6 Months</td><td>94.83</td><td>10.26%</td></tr></table></div>
  </aside>
  <h1 class="page-title">TELL US ABOUT YOUR ITEM</h1>
  <form class="item-form">
    <h2>INFORMATION IS NOT SHARED</h2>
    <div class="field-row">
      <div class="field"><input style="width:84px"><label>First</label></div>
      <div class="field"><input style="width:136px"><label style="text-align:left;padding-left:2px">Last</label></div>
    </div>
    <div class="field-row">
      <div class="field" style="display:flex;gap:8px;flex-wrap:wrap;width:142px"><input style="width:26px"><input style="width:36px"><input style="width:58px"><label style="width:100%;text-align:left;margin-top:0">Phone</label></div>
      <div class="field" style="margin-left:4px"><input style="width:136px"><label style="text-align:left">Email</label></div>
    </div>
    <div class="field" style="margin-top:10px"><textarea></textarea><label class="desc">Description of the item</label></div>
    <a class="btn">SUBMIT</a>
  </form>
  <footer class="site-footer">©2009 Aurum Exchange Australia Pty LTD</footer>
</section>

</body>
</html>
```